Super Cool Postcard Needed - design for animal chiropractor!

I need a postcard that will grab peoples attention for them to have their animal (dog,cat, horse) adjusted. I would prefer two sided post card - not to be mailed but to be handed out. The postcard needs to give them the info on why their pet would need to be adjusted. I included in the documents - photos, a flier and info on what animal chiropractic is. I would say to focus the flier on small animal but include horses (horse community is very familiar with chiropractic).

Target Market(s)

animal owners interested in wellness/holistic care for their pet

Font styles to use
Sans Serif

Colors

Designer to choose colors to be used in the design.

Requirements
Must have
• Logo, contact info, info on why a pet needs chiropractic, front and back design - not meant for mailing
Nice to have
• pictures
Should not have
• an area for an address

```html
<!DOCTYPE html>
<html lang="en">
<head>
<meta charset="UTF-8">
<title>Animal Chiropractic Postcard</title>
<link href="https://fonts.googleapis.com/css2?family=Montserrat:wght@700;800&family=Roboto+Condensed:wght@400;700&display=swap" rel="stylesheet">
<style>
:root{
  --bg:#e4e4e4;
  --black:#0b0b0b;
  --red:#d8202b;
  --white:#ffffff;
  --ink:#1a1a1a;
  --panel:#f2f2f2;
  --photo-warm:#b9a99a;
  --photo-cool:#8e969e;
}
*{margin:0;padding:0;box-sizing:border-box}
html,body{width:1200px;height:1000px;overflow:hidden;background:var(--bg)}
body{position:relative;font-family:"Roboto Condensed",Arial,sans-serif;color:var(--ink)}
.card{position:absolute;overflow:hidden}
.card-front{left:41px;top:35px;width:586px;height:453px;background:var(--panel)}
.card-back{left:569px;top:507px;width:584px;height:451px;background:var(--black)}
.front-bg{position:absolute;inset:0}
.brand-box{position:absolute;z-index:2;left:22px;top:23px;width:128px;height:115px;border:2px solid var(--white);background:var(--black);display:flex;flex-direction:column;align-items:center;justify-content:center;gap:12px}
.brand-dot{width:52px;height:52px;border-radius:50%;background:var(--red)}
.brand-name{font-family:"Montserrat",sans-serif;font-weight:800;font-size:9.5px;color:var(--white);white-space:nowrap}
.contact-top{position:absolute;z-index:2;left:129px;top:20px;width:420px;text-align:center;color:var(--white);white-space:nowrap}
.contact-top .lead{font-family:"Montserrat",sans-serif;font-weight:700;font-size:10.2px}
.contact-top .phone{font-family:"Montserrat",sans-serif;font-weight:800;font-size:19px;color:var(--red);margin-top:3px;letter-spacing:.5px}
.contact-top .web{font-family:"Montserrat",sans-serif;font-weight:700;font-size:10.5px;color:var(--red);margin-top:1px}
.front-photo{position:absolute;z-index:1;left:380px;top:80px;width:206px;height:373px;background:linear-gradient(90deg,var(--panel) 0%,rgba(242,242,242,0) 22%),linear-gradient(180deg,#d9d4cf 0%,var(--photo-warm) 35%,var(--photo-cool) 75%,#7d8187 100%)}
.front-text{position:absolute;z-index:2;left:38px;top:178px;width:400px}
.headline{font-family:"Montserrat",sans-serif;font-weight:800;font-size:19px;color:var(--red);letter-spacing:-.2px;white-space:nowrap}
.intro{font-family:"Montserrat",sans-serif;font-weight:700;font-size:10.5px;line-height:1.2;margin-top:2px;width:335px}
.intro .accent{color:var(--red)}
.list-title{font-weight:700;font-size:11.5px;margin-top:12px;margin-left:4px}
.bullets{list-style:none;margin-top:2px}
.bullets li{position:relative;padding-left:10px;font-size:10.3px;line-height:13.4px}
.bullets li::before{content:"";position:absolute;left:0;top:4.5px;width:5px;height:5px;background:var(--red)}
.front-text .bullets{margin-left:6px}
.closing{font-size:10.4px;line-height:13px;margin-top:13px;width:365px}

.back-main{position:absolute;left:0;top:0;width:376px;height:451px;background:var(--panel)}
.back-photo-faint{position:absolute;left:150px;top:120px;width:226px;height:331px;background:linear-gradient(160deg,#e6e6e6 0%,#cfcfcf 50%,#bdbdbd 100%)}
.what-block{position:absolute;left:0;top:0;width:376px;height:103px;background:var(--black);padding:19px 22px 0}
.section-title{font-weight:700;font-size:9.5px;color:var(--red);text-transform:uppercase}
.what-block p{color:var(--white);font-size:7.6px;line-height:11.2px;margin-top:2px}
.back-list{position:absolute;left:22px;width:345px}
.back-list .bullets li{font-size:8.2px;line-height:11.6px;padding-left:8px}
.back-list .bullets li::before{top:3px;width:4px;height:4px}
.age{font-size:8.2px;margin-top:11px}
.age b{color:var(--red);font-weight:700}
.back-side{position:absolute;left:379px;top:0;width:205px;height:451px;background:var(--black)}
.horse-photo{position:absolute;left:7px;top:18px;width:176px;height:235px;background:linear-gradient(180deg,#6a94c4 0%,#8fb0cf 35%,#5c7a4a 55%,#8c7a62 100%)}
.back-brand{position:absolute;left:0;top:268px;width:205px;text-align:center;color:var(--white)}
.back-brand .brand-dot{width:84px;height:84px;margin:0 auto 20px}
.back-brand .brand-name{font-size:12px}
.back-brand .phone{font-family:"Montserrat",sans-serif;font-weight:800;font-size:19px;margin-top:12px}
.back-brand .web{font-family:"Montserrat",sans-serif;font-weight:700;font-size:7px;margin-top:3px;white-space:nowrap}
</style>
</head>
<body>

<section class="card card-front">
  <svg class="front-bg" width="586" height="453" viewBox="0 0 586 453">
    <rect width="586" height="453" fill="#0b0b0b"/>
    <path d="M0,190 C150,130 330,85 586,72 L586,453 L0,453 Z" fill="#ffffff"/>
    <path d="M0,204 C150,146 330,102 586,88 L586,453 L0,453 Z" fill="#efefef"/>
  </svg>
  <div class="brand-box">
    <span class="brand-dot"></span>
    <span class="brand-name">DR. LAURA BENNETT</span>
  </div>
  <div class="contact-top">
    <div class="lead">To schedule an appointment or for more information, contact us at</div>
    <div class="phone">408- 555-0142</div>
    <div class="web">www.drlaurabennett.com/animal-chiropractic</div>
  </div>
  <div class="front-photo" role="img" aria-label="Photo of the smiling chiropractor holding a black puppy"></div>
  <div class="front-text">
    <h1 class="headline">CHIROPRACTIC CARE FOR YOUR PET!</h1>
    <p class="intro">Introducing <span class="accent">Dr. Laura Bennett</span>, chiropractor, who has been providing chiropractic care for over <span class="accent">15 years!</span></p>
    <p class="list-title">Your dog or cat can benefit from Chiropractic adjustments if they:</p>
    <ul class="bullets">
      <li>Have a limp that will not go away</li>
      <li>Do not want to jump in, out or on things as much or anymore</li>
      <li>Yelps with certain activities</li>
      <li>Are slow getting up or laying down</li>
      <li>Have been diagnosed with disc disease</li>
      <li>Wellness - prevention - a well moving spine will help prevent arthritis later in life</li>
      <li>They are in rehab from a current injury - sprain/strain, surgery</li>
      <li>Are involved in athletics - flyball, agility - top athletes receive regular chiropractic care</li>
      <li>Are working dogs - pulling wheelchairs, police dogs</li>
    </ul>
    <p class="closing">Animal chiropractic adjustments are not only for pets with injuries, it's great to start young so that we know how the spine/extremities are moving prior to &nbsp;a problem. &nbsp;Chiropractic adjustments definitely help with new and existing injuries. &nbsp;We also offer low level laser treatments to assist in the healing process.</p>
  </div>
</section>

<section class="card card-back">
  <div class="back-main">
    <div class="back-photo-faint" role="img" aria-label="Faded photo of a dog receiving an adjustment"></div>
    <div class="what-block">
      <h2 class="section-title">What is chiropractic ?</h2>
      <p>What is chiropractic - in simplest terms, a conservative approach to healthcare. &nbsp;We focus on the movement in the joints (spine/extremities) for the overall health and wellness of the pet. &nbsp;Restrictions in joint motion, can affect such things as athletic performance, normal biomechanics leading to repetitive stress injuries and sprain/strains. &nbsp;The issue, most restrictions in joint motions are subclinical and go undetected until they manifest into a problem.</p>
    </div>
    <div class="back-list" style="top:111px">
      <h2 class="section-title">Classic things chiropractic will help an animal with:</h2>
      <ul class="bullets">
        <li>post surgical (addressing compensatory gaits of (ex) TPLO surgeries)</li>
        <li>ambiguous limp, diagnostics come up clean</li>
        <li>dogs that have stopped jumping up on the couch or in and out of the car perhaps have fixations in the lower back or pelvis</li>
        <li>offers an alternative for treating acute and chronic musculoskeletal injuries without drugs</li>
        <li>senior pets moving better</li>
        <li>athletes - fly ball, agility, working</li>
        <li>working dogs - pulling, pushing, jumping</li>
        <li>wellness - prevention making sure joints are moving well to prevent arthritis</li>
        <li>pregnancy - helping the birthing process so the pelvis can move</li>
        <li>every test has been run, nothing seems to be helping the pet - send the hail mary pass</li>
      </ul>
      <p class="age"><b>AGE:</b>&nbsp; Age of pet - never too young or too old, puppies/kittens - seniors</p>
    </div>
    <div class="back-list" style="top:302px">
      <h2 class="section-title">Some signs/symptoms owners will report:</h2>
      <ul class="bullets">
        <li>Yelping in pain after a sudden movement when no other symptoms are present Weak front legs with no site of pain</li>
        <li>Looking, yelping or biting when being picked up around the chest area</li>
        <li>Hunched back</li>
        <li>Muscle spasms along the back</li>
        <li>Hip pain in the hind legs with no sign of canine arthritis</li>
        <li>Trouble standing or laying down</li>
        <li>Inability to jump</li>
        <li>Not wanting to perform normal work - i.e. pulling a wheel chair</li>
      </ul>
    </div>
  </div>
  <div class="back-side">
    <div class="horse-photo" role="img" aria-label="Photo of the chiropractor adjusting a horse outdoors"></div>
    <div class="back-brand">
      <div class="brand-dot"></div>
      <div class="brand-name">DR. LAURA BENNETT</div>
      <div class="phone">408- 555-0142</div>
      <div class="web">www.drlaurabennett.com/animal-chiropractic</div>
    </div>
  </div>
</section>

</body>
</html>
```